Lantern Hearthworks Business Cards

Looking to create simple business cards that highlight our unique three sided triangle fire pit design with the colors and font of our logo, listed below.

Colors

Designer to choose colors to be used in the design.

Requirements
Must have
• Looking for something simple that includes a picture of our fire pit with name, website (lanternhearthworks.com), phone number and email. Want to keep the color mostly orange and black.
• Font is gotham(medium) and orange color code is #ee6e22

```html
<!DOCTYPE html>
<html lang="en">
<head>
<meta charset="utf-8">
<title>Lantern Hearthworks Business Cards</title>
<link href="https://fonts.googleapis.com/css2?family=Montserrat:wght@500;600&family=Open+Sans:wght@400;600&display=swap" rel="stylesheet">
<style>
  :root {
    --stage: #8d8b8c;
    --card-dark: #2b2a2b;
    --card-dark-glow: #403e40;
    --paper: #ffffff;
    --ember: #ee6e22;
    --ink-light: #ffffff;
    --rule: #9a9a9a;
  }
  * { box-sizing: border-box; margin: 0; padding: 0; }
  html, body {
    width: 1200px; height: 880px; overflow: hidden;
    background: radial-gradient(circle at 40% 45%, #bdbcbd 0%, var(--stage) 55%, #5f5d5e 100%);
    font-family: "Open Sans", sans-serif;
  }
  .card {
    position: absolute;
    width: 540px; height: 309px;
    background: radial-gradient(circle at 60% 45%, var(--card-dark-glow) 0%, var(--card-dark) 70%);
    box-shadow: 0 10px 28px rgba(0,0,0,0.35);
    overflow: hidden;
  }
  .card--front { left: 60px; top: 90px; }
  .card--back { left: 600px; top: 480px; }

  .band { position: absolute; background: var(--paper); }
  .card--front .band--top { left: 0; top: 0; width: 100%; height: 15%; }
  .card--front .band--bottom { left: 0; bottom: 0; width: 100%; height: 15%; }
  .card--back .band--top { left: 0; top: 0; width: 48%; height: 36%; }
  .card--back .band--bottom { left: 0; bottom: 0; width: 62%; height: 32%; }

  .brand {
    position: absolute;
    display: flex; align-items: center; gap: 14px;
  }
  .brand__mark { width: 16px; height: 16px; background: var(--ember); flex: none; }
  .brand__divider { width: 1px; align-self: stretch; background: var(--rule); }
  .brand__name {
    font-family: "Montserrat", sans-serif;
    font-weight: 500;
    color: var(--ember);
    text-transform: uppercase;
    letter-spacing: 0.22em;
    line-height: 1.15;
  }
  .card--front .brand { left: 120px; top: 124px; height: 62px; }
  .card--front .brand__name { font-size: 22px; }
  .card--back .brand { left: 70px; top: 126px; height: 50px; }
  .card--back .brand__name { font-size: 16px; }

  .contact {
    position: absolute; left: 320px; top: 92px; width: 200px;
    color: var(--ember);
  }
  .contact__name {
    font-weight: 600; font-size: 17px; color: var(--ink-light);
  }
  .contact__role { font-size: 13px; margin-bottom: 6px; }
  .contact__rule { height: 1px; background: var(--ink-light); margin-bottom: 10px; }
  .contact__list { list-style: none; font-size: 11.5px; }
  .contact__list li { display: flex; align-items: center; gap: 8px; margin-bottom: 6px; }
  .contact__list svg { width: 12px; height: 12px; flex: none; fill: var(--ink-light); }
</style>
</head>
<body>
  <section class="card card--front" aria-label="Business card front">
    <div class="band band--top"></div>
    <div class="band band--bottom"></div>
    <div class="brand">
      <span class="brand__mark"></span>
      <span class="brand__divider"></span>
      <span class="brand__name">Lantern<br>Hearthworks</span>
    </div>
  </section>

  <section class="card card--back" aria-label="Business card back">
    <div class="band band--top"></div>
    <div class="band band--bottom"></div>
    <div class="brand">
      <span class="brand__mark"></span>
      <span class="brand__divider"></span>
      <span class="brand__name">Lantern<br>Hearthworks</span>
    </div>
    <div class="contact">
      <p class="contact__name">Dana Reyes</p>
      <p class="contact__role">Founder/CEO</p>
      <div class="contact__rule"></div>
      <ul class="contact__list">
        <li><svg viewBox="0 0 12 12"><path d="M0 2h12v8H0z M0 2l6 4 6-4" fill="#fff" stroke="#2b2a2b" stroke-width="0.8"/></svg>hello@lanternhearthworks.com</li>
        <li><svg viewBox="0 0 12 12"><path d="M3 1l2 2-1 1.5c.8 1.6 2 2.8 3.5 3.5L9 7l2 2-1.5 2C5 10.5 1.5 7 1 2.5z"/></svg>555-210-4471</li>
        <li><svg viewBox="0 0 12 12"><path d="M1 4c2-2 8-2 10 0v2H8V5H4v1H1z M2 7h8v4H2z"/></svg>555-210-4480</li>
        <li><svg viewBox="0 0 12 12"><path d="M1 2h10v7H1z M4 11h4v-1H4z" fill="none" stroke="#fff" stroke-width="1"/></svg>lanternhearthworks.com</li>
      </ul>
    </div>
  </section>
</body>
</html>
```